Pinecrest Relay Group VoIP YOUR BUSINESS ON THE CLOUD

we are a local VoIP Company. We provide telephone lines for Business as well as Phone hardware... We would like to use an intro offer of free telephone lines for your business as a catch. We help companies save over 35% on their monthly phone bills, we offer powerful features, easy to use and set up. Your business on the cloud is our catch phrase.. We want our customers to know that we are a true VoIP company offering Unlimited local and long distance plans, Never metered billing, we offer free phones.. we want a double sided modern eye catching flyer. Our company colors are Neon Orange and a sky blue..

Target Market(s)

Small to medium business

Industry/Entity Type

Business

Font styles to use
Serif

Colors
f78f20
34a6d7
faa54b
85cae6

Requirements
Must have
• color eye catching
• Receive your primary telephone number free as the eye catcher!!!
Should not have
• Please do not list any of our pricing on the flyer.

```html
<!DOCTYPE html>
<html lang="en">
<head>
<meta charset="utf-8">
<title>Pinecrest Relay Group – Your Business on the Cloud</title>
<link href="https://fonts.googleapis.com/css2?family=Open+Sans:wght@400;600;700;800&display=swap" rel="stylesheet">
<style>
  :root{
    --orange:#f78f20;
    --orange-light:#faa54b;
    --orange-deep:#e8731a;
    --sky:#34a6d7;
    --sky-light:#85cae6;
    --sky-pale:#cfeaf6;
    --ink:#222a30;
    --white:#ffffff;
  }
  *{box-sizing:border-box;margin:0;padding:0}
  html,body{width:853px;height:1200px;overflow:hidden;background:var(--white)}
  body{font-family:"Open Sans",Arial,sans-serif;color:var(--ink)}
  .flyer{position:relative;width:853px;height:1200px;overflow:hidden;
    background:linear-gradient(180deg,#ffffff 0%,#f2f9fd 18%,var(--sky-pale) 38%,var(--sky-light) 60%,#bfe3f3 78%,#ffffff 90%)}
  .sky-scene{position:absolute;inset:0;
    background:radial-gradient(ellipse 520px 160px at 20% 98%,rgba(255,255,255,.95),rgba(255,255,255,0) 70%),
               radial-gradient(ellipse 560px 180px at 85% 96%,rgba(255,255,255,.95),rgba(255,255,255,0) 70%),
               radial-gradient(ellipse 360px 120px at 10% 48%,rgba(255,255,255,.6),rgba(255,255,255,0) 70%)}

  .brand-name{font-weight:800;color:var(--sky);line-height:1.1;letter-spacing:.3px}
  .brand-top{position:absolute;left:100px;top:40px;z-index:2}
  .brand-top .brand-name{font-size:26px}

  .desk-phone{position:absolute;left:0;top:140px;width:370px;height:340px;border-radius:0 18px 18px 0;
    background:linear-gradient(160deg,#4a4f55 0%,#24282c 55%,#15181b 100%)}

  .offer-banner{position:absolute;right:0;top:0;width:540px;height:290px}

  .cloud-tag{position:absolute;left:440px;top:278px;width:413px;height:160px}
  .cloud-tag svg{position:absolute;left:0;top:0}
  .cloud-tag p{position:absolute;color:var(--sky);font-size:34px;line-height:1.2;white-space:nowrap}
  .cloud-tag .line1{left:80px;top:44px;font-weight:600}
  .cloud-tag .line2{left:105px;top:88px;font-weight:700}

  .savings{position:absolute;left:120px;top:505px}
  .savings .lead{font-size:42px;font-weight:400;line-height:1.1}
  .savings .headline{font-size:64px;font-weight:800;line-height:1.1;letter-spacing:-1px}
  .savings .tail{font-size:28px;font-weight:400;line-height:1.25}
  .percent-badge{position:absolute;left:525px;top:510px;width:200px;height:200px;border-radius:50%;
    background:var(--orange);color:var(--white);display:flex;align-items:center;justify-content:center;
    font-size:72px;font-weight:800;font-style:italic;letter-spacing:-2px}

  .features{position:absolute;left:113px;top:765px;width:600px;display:flex}
  .feature{width:200px;text-align:center}
  .feature-icon{width:92px;height:92px;border-radius:50%;background:var(--orange);margin:0 auto 14px;
    display:flex;align-items:center;justify-content:center}
  .feature-label{font-size:24px;font-weight:600;line-height:1.2}

  .footer{position:absolute;left:0;top:1010px;width:853px;height:170px}
  .brand-foot{position:absolute;left:43px;top:30px}
  .brand-foot .brand-name{font-size:28px}
  .call-block{position:absolute;left:335px;top:62px}
  .call-line{font-size:14px;font-weight:800;font-style:italic;letter-spacing:.2px;white-space:nowrap}
  .phone-pill{margin-top:10px;width:248px;height:44px;border-radius:22px;background:var(--orange);
    display:flex;align-items:center;justify-content:center;gap:10px;color:var(--white);font-size:24px;font-weight:700}
  .social{position:absolute;left:668px;top:58px;display:flex;gap:8px}
  .social span{width:30px;height:30px;border-radius:4px;display:block}
  .social .s1{background:#3b5998}
  .social .s2{background:var(--sky)}
  .web{position:absolute;left:640px;top:102px;font-size:13px;color:var(--sky);font-weight:600;white-space:nowrap}
</style>
</head>
<body>
<main class="flyer">
  <div class="sky-scene" role="img" aria-label="Bright sky with soft white clouds"></div>

  <div class="desk-phone" role="img" aria-label="Photo of a black office desk phone with handset, colour display and keypad"></div>

  <div class="brand-top">
    <p class="brand-name">Pinecrest Relay<br>Group</p>
  </div>

  <svg class="offer-banner" viewBox="0 0 540 290" aria-label="We offer free telephone lines for your business">
    <g transform="rotate(-8 270 135)">
      <rect x="30" y="10" width="600" height="80" fill="#faa54b"/>
      <rect x="10" y="90" width="620" height="80" fill="#e8731a"/>
      <rect x="40" y="170" width="590" height="66" fill="#f78f20"/>
      <text x="70" y="68" fill="#fff" font-family="Open Sans, sans-serif" font-weight="800" font-size="42" textLength="320" lengthAdjust="spacingAndGlyphs">WE OFFER FREE</text>
      <text x="34" y="150" fill="#fff" font-family="Open Sans, sans-serif" font-weight="800" font-size="52" textLength="440" lengthAdjust="spacingAndGlyphs">TELEPHONE LINES</text>
      <text x="66" y="218" fill="#fff" font-family="Open Sans, sans-serif" font-weight="800" font-size="38" textLength="400" lengthAdjust="spacingAndGlyphs">FOR YOUR BUSINESS</text>
    </g>
  </svg>

  <div class="cloud-tag">
    <svg width="413" height="160" viewBox="0 0 413 160" aria-hidden="true">
      <path d="M40,150 C5,150 0,100 35,92 C30,52 82,36 108,58 C128,16 200,6 230,42 C265,12 335,22 342,68 C380,62 413,80 413,100 L413,150 Z" fill="#ffffff"/>
    </svg>
    <p class="line1">Your business</p>
    <p class="line2">on the Cloud</p>
  </div>

  <section class="savings">
    <p class="lead">We help companies</p>
    <p class="headline">SAVE OVER</p>
    <p class="tail">on their monthly phone bills</p>
  </section>
  <div class="percent-badge">35%</div>

  <section class="features">
    <div class="feature">
      <div class="feature-icon">
        <svg width="48" height="48" viewBox="0 0 56 56" fill="none" stroke="#fff" stroke-width="3" stroke-linecap="round">
          <path d="M20 34c-4-3-6-7-6-11a14 14 0 0 1 28 0c0 4-2 8-6 11v6H20z"/>
          <line x1="21" y1="46" x2="35" y2="46"/><line x1="24" y1="51" x2="32" y2="51"/>
          <line x1="28" y1="2" x2="28" y2="5"/><line x1="8" y1="10" x2="10" y2="12"/><line x1="48" y1="10" x2="46" y2="12"/>
        </svg>
      </div>
      <p class="feature-label">Powerful<br>features</p>
    </div>
    <div class="feature">
      <div class="feature-icon">
        <svg width="50" height="45" viewBox="0 0 58 52" fill="none" stroke="#fff" stroke-width="3" stroke-linejoin="round">
          <path d="M4 6h30v20H16l-8 7v-7H4z"/>
          <path d="M38 16h16v20h-4v7l-8-7H24v-6"/>
          <circle cx="12" cy="16" r="1.5" fill="#fff"/><circle cx="19" cy="16" r="1.5" fill="#fff"/><circle cx="26" cy="16" r="1.5" fill="#fff"/>
        </svg>
      </div>
      <p class="feature-label">Easy<br>to use</p>
    </div>
    <div class="feature">
      <div class="feature-icon">
        <svg width="48" height="48" viewBox="0 0 56 56" fill="none" stroke="#fff" stroke-width="3" stroke-linecap="round" stroke-linejoin="round">
          <path d="M10 46l22-22"/><path d="M30 12a10 10 0 0 0 14 14l-6-6 2-6 6-2"/>
          <path d="M10 10l14 14"/><path d="M6 14l8-8 4 4-8 8z"/><path d="M34 34l12 12-4 4-12-12"/>
        </svg>
      </div>
      <p class="feature-label">Easy<br>set up</p>
    </div>
  </section>

  <footer class="footer">
    <div class="brand-foot">
      <p class="brand-name">Pinecrest Relay<br>Group</p>
    </div>
    <div class="call-block">
      <p class="call-line">CALL TODAY FOR YOUR FREE PHONES</p>
      <div class="phone-pill">
        <svg width="20" height="20" viewBox="0 0 24 24" aria-hidden="true">
          <path fill="#fff" d="M6.6 10.8a15 15 0 0 0 6.6 6.6l2.2-2.2a1 1 0 0 1 1-.25 11.4 11.4 0 0 0 3.6.57 1 1 0 0 1 1 1V20a1 1 0 0 1-1 1A17 17 0 0 1 3 4a1 1 0 0 1 1-1h3.5a1 1 0 0 1 1 1c0 1.25.2 2.45.57 3.57a1 1 0 0 1-.25 1z"/>
        </svg>
        <span>555-014-2870</span>
      </div>
    </div>
    <div class="social"><span class="s1"></span><span class="s2"></span></div>
    <p class="web">www.pinecrestrelay.com</p>
  </footer>
</main>
</body>
</html>
```